TALLYMORA (www.tallymora.com.zz) needs exciting professional Business Cards

TALLYMORA is an exciting new start-up targeting innovative ways to engage with retail customers at the point of sale.
Our Vision
Through applying new thinking to an old business we are reinventing selected segments of the Australian retail messaging industry, generating significant value for our customers, our suppliers, and our owners.
We operate with integrity, agility, and intelligence to doing things smarter, faster and more efficiently.
We bring deep industry expertise, deep relationships with customers and suppliers, and a will to see the old ways give way to smarter ways – this is why we win.
From this economically sustainable platform, we will examine the disruption of other market segments by further leveraging the elements that make us successful.
Our Values
With our clients, with our suppliers, with our staff, and with our owners:
# We Partner – We align the interest of all stakeholders by striving to ensure everything we do is mutually beneficial and commercially sustainable in the long term. We are clear with all our stakeholders about what our expectations are of them, and we seek clarity from them in their expectations of us.
# We Innovate – In the segments we choose to compete in, we bring fresh ideas, new business processes, the right relationships, and the right technology to ensure the supply chain is nimble, competitive, and reliable.
# We are Accountable – We say what we will do, and then do what we say.
# We Perform – We use our skills, relationships, and reputation to deliver value to our customers, suppliers, and owners.
Initially we are building our business from low-tech through printing promotional offers and retailer messages on ATM and EFTPOS receipts, but as soon as cash flow supports it we will be engaging in high-tech real-time targeted offers to the specific consumer.
I'd like the cards to reflect our values.
Please check out the web site we have just launched - it is pretty basic but it has only been up a week. We intend to sharpen it over the coming weeks, but you'll get the idea of what our core messages are.
I have recently sourced a logo from SketchHive, and have attached the source files for use.
Personal information to include:
Name: FirstName Surname
Title: Managing Director
email: first.surname@tallymora.com.zz
Mobile: +61-472-555-318
Generic Co Details to include:
Web: www.tallymora.com.zz
email: tallymora@tallymora.com.zz
Fax: +61-8-5037-2164
Offices & Agents: Sydney, Melbourne, Brisbane, Adelaide, Perth
Byline: Innovation . Integrity . Service
Target Market(s)
Our customers are large corporations that have professional Point Of Sale marketing experts looking for a supplier with an edge over others in a crowded market. The buyer of our product and services is ultimately a communications expert.
They want to see distinctive competence, and an agility of thinking that will make them money through driving more consumer spending.
Industry/Entity Type
Retail
Look and feel
Each slider illustrates characteristics of the customer's brand and the style your logo design should communicate.

```html
<!DOCTYPE html>
<html lang="en">
<head>
<meta charset="utf-8">
<title>TALLYMORA Business Cards</title>
<link rel="stylesheet" href="https://fonts.googleapis.com/css2?family=Arimo:wght@400;700&display=swap">
<style>
  :root {
    --backdrop: #1e1f21;
    --brand-blue: #1677b8;
    --brand-blue-light: #2a9fd4;
    --brand-blue-dark: #0e6bae;
    --card-white: #f1f1f0;
    --ink-grey: #6b6b6b;
    --rule-grey: #c9c9c9;
    --white: #ffffff;
  }
  * { margin: 0; padding: 0; box-sizing: border-box; }
  html, body {
    width: 1200px;
    height: 896px;
    overflow: hidden;
    background: var(--backdrop);
    font-family: "Arimo", Arial, sans-serif;
  }
  .canvas {
    position: relative;
    width: 1200px;
    height: 896px;
  }
  .card {
    position: absolute;
    left: 354px;
    width: 484px;
    height: 268px;
  }
  /* Front */
  .card-front {
    top: 165px;
    background: linear-gradient(160deg, var(--brand-blue-light) 0%, var(--brand-blue-dark) 100%);
    color: var(--white);
  }
  .card-front .wordmark {
    position: absolute;
    left: 0;
    right: 0;
    top: 100px;
    display: flex;
    justify-content: center;
    align-items: center;
    gap: 16px;
  }
  .card-front .wordmark-name {
    font-weight: 700;
    font-size: 52px;
    letter-spacing: -1px;
    line-height: 1;
    color: var(--white);
  }
  .card-front .tagline {
    position: absolute;
    left: 0;
    right: 0;
    top: 212px;
    text-align: center;
    font-size: 15px;
    color: var(--white);
  }
  /* Back */
  .card-back {
    top: 473px;
    background: var(--card-white);
    color: var(--ink-grey);
  }
  .card-back .wordmark {
    position: absolute;
    left: 33px;
    top: 34px;
    display: flex;
    align-items: center;
    gap: 12px;
  }
  .card-back .wordmark-name {
    font-weight: 700;
    font-size: 40px;
    letter-spacing: -0.5px;
    line-height: 1;
    color: var(--brand-blue);
  }
  .person {
    position: absolute;
    left: 33px;
    top: 125px;
    display: flex;
    align-items: baseline;
    gap: 10px;
  }
  .person-name { font-size: 17px; color: var(--ink-grey); }
  .person-title { font-size: 14px; color: var(--brand-blue); text-transform: uppercase; letter-spacing: 0.3px; }
  .contact-list {
    position: absolute;
    left: 33px;
    top: 160px;
    font-size: 12.5px;
    line-height: 18.5px;
    list-style: none;
  }
  .contact-label { color: var(--brand-blue); margin-right: 4px; }
  .contact-value { margin-right: 6px; }
  .rule {
    position: absolute;
    left: 33px;
    width: 368px;
    top: 221px;
    border-top: 1px solid var(--rule-grey);
  }
  .website {
    position: absolute;
    left: 33px;
    top: 231px;
    font-size: 12.5px;
    color: var(--ink-grey);
  }
</style>
</head>
<body>
<main class="canvas">
  <section class="card card-front" aria-label="Business card front">
    <div class="wordmark">
      <span class="wordmark-name">TALLYMORA</span>
      <svg width="44" height="44" viewBox="0 0 44 44" aria-hidden="true">
        <circle cx="22" cy="22" r="19" fill="none" stroke="#ffffff" stroke-width="3"/>
      </svg>
    </div>
    <p class="tagline">Innovation | Integrity | Service</p>
  </section>

  <section class="card card-back" aria-label="Business card back">
    <div class="wordmark">
      <span class="wordmark-name">TALLYMORA</span>
      <svg width="36" height="36" viewBox="0 0 36 36" aria-hidden="true">
        <circle cx="18" cy="18" r="15.5" fill="none" stroke="#1677b8" stroke-width="2"/>
      </svg>
    </div>
    <div class="person">
      <span class="person-name">FirstName Surname</span>
      <span class="person-title">Managing Director</span>
    </div>
    <ul class="contact-list">
      <li><span class="contact-label">mobile</span><span class="contact-value">+61-472-555-318</span> <span class="contact-label">email</span><span class="contact-value">first.surname@tallymora.com.zz</span></li>
      <li><span class="contact-label">fax</span><span class="contact-value">+61-8-5037-2164</span> <span class="contact-label">email</span><span class="contact-value">tallymora@tallymora.com.zz</span></li>
      <li>Sydney, Melbourne, Brisbane, Adelaide, Perth</li>
    </ul>
    <div class="rule"></div>
    <p class="website">www.tallymora.com.zz</p>
  </section>
</main>
</body>
</html>
```